Design some Business Cards for Tot's Treasure

Need some really cool, innovative business cards, using our logo, but making the design really different and interesting.
Use colors like lime green and pink, anything bright and interesting. Be innovative.

```html
<!DOCTYPE html>
<html lang="en">
<head>
<meta charset="utf-8">
<title>Tot's Treasure – Business Cards</title>
<link href="https://fonts.googleapis.com/css2?family=Open+Sans:wght@400;600;700&display=swap" rel="stylesheet">
<style>
  :root {
    --canvas: #eee9e3;
    --card-white: #ffffff;
    --card-pink: #ecc9bf;
    --red: #e2202c;
    --purple: #7b2a8c;
    --ink: #333333;
    --muted: #8a8a8a;
    --art-light: #f1f1f1;
    --art-pink: #e3b9ae;
  }
  * { box-sizing: border-box; margin: 0; padding: 0; }
  html, body { width: 1200px; height: 1023px; overflow: hidden; }
  body {
    background: var(--canvas);
    font-family: "Open Sans", sans-serif;
    position: relative;
  }
  .card {
    position: absolute;
    border-radius: 22px;
    overflow: hidden;
    box-shadow: 0 10px 28px rgba(0,0,0,0.18);
  }
  /* front */
  .card-front {
    left: 60px; top: 330px;
    width: 620px; height: 354px;
    background: var(--card-white);
  }
  .front-art {
    position: absolute;
    left: 300px; top: 26px;
    width: 230px; height: 200px;
    border-radius: 50%;
    background: var(--art-light);
  }
  .edge-band {
    position: absolute;
    right: 0; top: 0;
    width: 34px; height: 100%;
    display: flex; flex-direction: column;
  }
  .edge-band .band-red { flex: 1; background: var(--red); }
  .edge-band .band-purple { flex: 1; background: var(--purple); }
  .brand {
    display: flex; align-items: center; gap: 10px;
  }
  .brand-dot {
    width: 22px; height: 22px; border-radius: 50%;
    background: var(--red);
    flex: none;
  }
  .brand-name {
    color: var(--purple);
    font-weight: 700;
    font-size: 22px;
    white-space: nowrap;
  }
  .card-front .brand {
    position: absolute; left: 34px; top: 118px;
  }
  .person {
    position: absolute; left: 34px; top: 166px;
  }
  .person-name {
    color: var(--red);
    font-weight: 700;
    font-size: 19px;
  }
  .person-role {
    color: var(--muted);
    font-size: 12px;
    margin-top: 1px;
  }
  .contact-list {
    position: absolute; left: 34px; top: 222px;
    list-style: none;
  }
  .contact-list li {
    display: flex; align-items: center; gap: 9px;
    color: var(--red);
    font-size: 12.5px;
    line-height: 19px;
  }
  .contact-list .icon {
    width: 13px; height: 13px; flex: none;
    background: var(--muted);
    border-radius: 2px;
    display: flex; align-items: center; justify-content: center;
  }
  .contact-list .icon svg { width: 9px; height: 9px; }
  .contact-list .indent { padding-left: 22px; }
  /* back */
  .card-back {
    left: 770px; top: 200px;
    width: 354px; height: 620px;
    background: var(--card-pink);
  }
  .back-art {
    position: absolute;
    left: 20px; top: -60px;
    width: 300px; height: 260px;
    border-radius: 50%;
    background: var(--art-pink);
  }
  .back-logo {
    position: absolute;
    left: 0; right: 0; top: 400px;
    display: flex; justify-content: center;
  }
  .back-logo .brand-name { font-size: 26px; }
  .back-logo .brand-dot { width: 26px; height: 26px; }
</style>
</head>
<body>

<section class="card card-front" aria-label="Business card front">
  <div class="front-art" role="img" aria-label="Hand-drawn line illustration of a smiling baby"></div>
  <div class="edge-band"><span class="band-red"></span><span class="band-purple"></span></div>

  <div class="brand">
    <span class="brand-dot"></span>
    <span class="brand-name">Tot's Treasure</span>
  </div>

  <div class="person">
    <p class="person-name">Mara Ellis</p>
    <p class="person-role">Owner</p>
  </div>

  <ul class="contact-list">
    <li><span class="icon"><svg viewBox="0 0 10 10"><path d="M2 1h2l1 2-1 1a5 5 0 0 0 2 2l1-1 2 1v2c-4 0-7-3-7-7z" fill="#fff"/></svg></span>0410-372-5160</li>
    <li><span class="icon"><svg viewBox="0 0 10 10"><rect x="2" y="1" width="6" height="8" rx="1" fill="#fff"/></svg></span>00 987 654 321</li>
    <li><span class="icon"><svg viewBox="0 0 10 10"><rect x="1" y="2.5" width="8" height="5" fill="#fff"/><path d="M1 2.5l4 3 4-3" stroke="#8a8a8a" stroke-width="0.8" fill="none"/></svg></span>mara@totstreasure.com</li>
    <li><span class="icon"><svg viewBox="0 0 10 10"><circle cx="5" cy="5" r="3.6" stroke="#fff" stroke-width="1" fill="none"/><path d="M1.4 5h7.2M5 1.4v7.2" stroke="#fff" stroke-width="0.8"/></svg></span>www.totstreasure.com</li>
    <li><span class="icon"><svg viewBox="0 0 10 10"><path d="M5 9S2 5.6 2 3.8a3 3 0 0 1 6 0C8 5.6 5 9 5 9z" fill="#fff"/></svg></span>4421 Maple Grove Ave.Suite 12</li>
    <li class="indent">Riverton OR 97321</li>
  </ul>
</section>

<section class="card card-back" aria-label="Business card back">
  <div class="back-art" role="img" aria-label="Hand-drawn line illustration of a baby peeking over the top edge"></div>
  <div class="back-logo">
    <div class="brand">
      <span class="brand-dot"></span>
      <span class="brand-name">Tot's Treasure</span>
    </div>
  </div>
</section>

</body>
</html>
```